Marrowind Exteriors

Design 2-3 branded image ads using all for provided logos. each ad is for a roof replacement. The offer is, buy a new roof and receive a free gutter replacement, and 10 years of free rood maintenance. These must be included. What's optional ? you have the option the mention 50 year warranty, 25 year workmanship warranty. You also have an option to use price offer of $17,997.

```html
<!DOCTYPE html>
<html lang="en">
<head>
<meta charset="utf-8">
<title>Marrowind Exteriors – Roof Replacement Ads</title>
<link href="https://fonts.googleapis.com/css2?family=Bebas+Neue&family=Anton&family=Poppins:wght@500;600;700&display=swap" rel="stylesheet">
<style>
  :root {
    --forest: #263a32;
    --forest-deep: #1f2f29;
    --lime: #8dc63f;
    --white: #ffffff;
    --board: #ececec;
    --shadow: #b9bcbb;
    --seal-dark: #2b2b2b;
    --seal-red: #d7262d;
    --seal-blue: #1d3f7a;
  }
  * { margin: 0; padding: 0; box-sizing: border-box; }
  html, body { width: 1200px; height: 666px; overflow: hidden; }
  body {
    background: linear-gradient(180deg, #f7f7f7 0%, var(--board) 100%);
    position: relative;
    font-family: "Poppins", sans-serif;
  }
  .ad-shadow {
    position: absolute; width: 529px; height: 529px;
    background: var(--shadow); filter: blur(6px); opacity: .7;
  }
  .ad {
    position: absolute; top: 69px; width: 529px; height: 529px;
    overflow: hidden; background: var(--forest);
  }
  .ad--crew { left: 49px; }
  .ad--gutter { left: 623px; }
  .abs { position: absolute; }

  .headline {
    font-family: "Bebas Neue", sans-serif;
    font-size: 58px; line-height: 53px; letter-spacing: .5px;
    color: var(--white); text-transform: uppercase;
    text-shadow: 2px 3px 4px rgba(0,0,0,.35);
  }
  .headline .accent { color: var(--lime); }
  .years {
    font-family: "Poppins", sans-serif; font-weight: 700;
    font-size: 31px; line-height: 34px; color: var(--lime);
  }
  .years-note {
    font-family: "Poppins", sans-serif; font-weight: 500;
    font-size: 17.5px; line-height: 23px; color: var(--white);
  }
  .brand {
    display: flex; flex-direction: column; align-items: center; gap: 8px;
    font-family: "Poppins", sans-serif; font-weight: 600;
    font-size: 12.5px; line-height: 14px; letter-spacing: 1px;
    color: var(--white); text-transform: uppercase; text-align: center;
  }
  .brand-mark { width: 30px; height: 30px; background: var(--lime); }
  .seals { display: flex; align-items: center; gap: 12px; }
  .seal { width: 42px; height: 42px; }
  .seal--dark { width: 28px; background: var(--seal-dark); border-radius: 3px; }
  .seal--red { background: var(--seal-red); }
  .seal--blue { width: 30px; height: 30px; background: var(--seal-blue); transform: rotate(45deg); margin: 0 6px; border: 2px solid #c9a949; }

  .perks {
    border: 1px solid rgba(255,255,255,.8);
    width: 155px; height: 195px;
  }
  .perk {
    position: absolute; left: 43px;
    font-family: "Anton", sans-serif; font-size: 15.5px; line-height: 17.5px;
    color: var(--white); letter-spacing: .2px;
  }
  .perk .accent { color: var(--lime); }
  .perk-icon { position: absolute; left: 16px; width: 12px; height: 12px; }
</style>
</head>
<body>

  <!-- Ad 1: crew on roof -->
  <div class="ad-shadow" style="left:63px; top:83px;"></div>
  <section class="ad ad--crew">
    <div class="abs" role="img" aria-label="Roofer in hard hat and safety vest fastening shingles with a drill on a sloped roof under a blue sky"
         style="inset:0; background: linear-gradient(160deg, #8fb0cf 0%, #b9cde0 35%, #7a5a44 55%, #5b4233 80%, #3d2d24 100%);"></div>
    <svg class="abs" style="inset:0" width="529" height="529" viewBox="0 0 529 529" aria-hidden="true">
      <defs>
        <linearGradient id="crewFade" x1="0" y1="0" x2="1" y2="0">
          <stop offset="0" stop-color="#263a32" stop-opacity=".85"/>
          <stop offset=".55" stop-color="#263a32" stop-opacity=".35"/>
          <stop offset="1" stop-color="#263a32" stop-opacity="0"/>
        </linearGradient>
      </defs>
      <rect x="0" y="300" width="529" height="229" fill="url(#crewFade)"/>
      <path d="M0 0 H529 V180 C529 230 470 250 400 290 C330 330 300 315 220 315 L0 315 Z" fill="#263a32"/>
      <line x1="494" y1="123" x2="494" y2="496" stroke="#fff" stroke-width="1"/>
      <line x1="192" y1="496" x2="494" y2="496" stroke="#fff" stroke-width="1"/>
      <circle cx="494" cy="123" r="3" fill="#fff"/>
      <circle cx="192" cy="496" r="3" fill="#fff"/>
    </svg>

    <h1 class="headline abs" style="left:44px; top:41px;">
      Buy a new roof<br>and receive a<br>
      <span class="accent">Free gutter<br>replacement</span>
    </h1>

    <div class="brand abs" style="left:395px; top:45px; width:110px;">
      <span class="brand-mark"></span>
      <span>Marrowind<br>Exteriors</span>
    </div>

    <p class="years abs" style="left:44px; top:303px;">10 YEARS</p>
    <p class="years-note abs" style="left:44px; top:340px;">of free roof<br>maintenance<br>included.</p>

    <div class="seals abs" style="left:44px; top:458px;" aria-label="Partner seals">
      <span class="seal seal--dark"></span>
      <span class="seal seal--red"></span>
      <span class="seal seal--blue"></span>
    </div>
  </section>

  <!-- Ad 2: gutter close-up -->
  <div class="ad-shadow" style="left:637px; top:83px;"></div>
  <section class="ad ad--gutter">
    <div class="abs" role="img" aria-label="Close-up of a new dark shingle roof edge with a metal gutter running along it, chimney against a cloudy sky"
         style="inset:0; background: linear-gradient(200deg, #d9e2ec 0%, #a8b6c6 18%, #6b7684 40%, #4b535d 65%, #3a4048 100%);"></div>
    <svg class="abs" style="inset:0" width="529" height="529" viewBox="0 0 529 529" aria-hidden="true">
      <defs>
        <linearGradient id="gutterFade" x1="0" y1="0" x2="0" y2="1">
          <stop offset="0" stop-color="#263a32" stop-opacity="0"/>
          <stop offset="1" stop-color="#263a32" stop-opacity=".75"/>
        </linearGradient>
      </defs>
      <rect x="209" y="260" width="320" height="269" fill="url(#gutterFade)"/>
      <rect x="0" y="0" width="209" height="529" fill="#263a32" opacity=".93"/>
      <line x1="494" y1="123" x2="494" y2="470" stroke="#fff" stroke-width="1"/>
      <line x1="317" y1="470" x2="494" y2="470" stroke="#fff" stroke-width="1"/>
      <circle cx="494" cy="123" r="3" fill="#fff"/>
    </svg>

    <div class="brand abs" style="left:24px; top:51px; width:110px;">
      <span class="brand-mark"></span>
      <span>Marrowind<br>Exteriors</span>
    </div>

    <div class="seals abs" style="left:357px; top:50px;" aria-label="Partner seals">
      <span class="seal seal--dark"></span>
      <span class="seal seal--red"></span>
      <span class="seal seal--blue"></span>
    </div>

    <h1 class="headline abs" style="left:35px; top:163px;">
      <span class="accent">Buy a new roof<br>and receive a</span>
    </h1>
    <h2 class="headline abs" style="left:225px; top:276px;">Free gutter<br>replacement</h2>

    <div class="perks abs" style="left:36px; top:279px;">
      <svg class="perk-icon" style="top:32px" viewBox="0 0 12 12" aria-hidden="true"><path d="M1.5 6.5 L4.5 9.5 L10.5 2.5" fill="none" stroke="#8dc63f" stroke-width="2"/></svg>
      <p class="perk" style="top:27px;"><span class="accent">50-YEAR</span><br>warranty</p>
      <svg class="perk-icon" style="top:81px" viewBox="0 0 12 12" aria-hidden="true"><path d="M1.5 6.5 L4.5 9.5 L10.5 2.5" fill="none" stroke="#8dc63f" stroke-width="2"/></svg>
      <p class="perk" style="top:76px;"><span class="accent">25-YEAR</span><br>workmanship<br>warranty</p>
      <svg class="perk-icon" style="top:152px" viewBox="0 0 12 12" aria-hidden="true"><path d="M1.5 6.5 L4.5 9.5 L10.5 2.5" fill="none" stroke="#8dc63f" stroke-width="2"/></svg>
      <p class="perk" style="top:148px;">Price offer of<br><span class="accent">$17,997</span></p>
    </div>

    <p class="years abs" style="left:225px; top:396px;">10 YEARS</p>
    <p class="years-note abs" style="left:225px; top:433px; line-height:20px;">of free roof maintenance<br>included.</p>
  </section>

</body>
</html>
```